" Possui corretores credenciados que vendem lotes e terrenos no Vale do Paraíba. A empresa não possui escritório próprio, os corretores trabalham nos plantões de vendas das incorporadoras. "

```html
<!DOCTYPE html>
<html lang="pt-BR">
<head>
<meta charset="UTF-8">
<title>Vallora Imóveis — Pasta</title>
<link rel="stylesheet" href="https://fonts.googleapis.com/css2?family=Montserrat:wght@400;500;600&display=swap">
<style>
  :root {
    --bg: #e9e9e9;
    --paper: #ffffff;
    --cover: #2b2b2b;
    --gold: #f4b22c;
    --ink: #3a3a3a;
    --muted: #7a7a7a;
  }
  * { box-sizing: border-box; margin: 0; padding: 0; }
  html, body {
    width: 1200px; height: 1200px; overflow: hidden;
    background: var(--bg);
    font-family: "Montserrat", sans-serif;
  }
  .folder {
    position: absolute;
    left: 50px; top: 215px;
    width: 1100px; height: 770px;
    display: flex;
    box-shadow: 0 6px 18px rgba(0,0,0,0.18);
  }
  .letterhead, .cover {
    position: relative;
    width: 50%; height: 100%;
  }
  .letterhead { background: var(--paper); }
  .cover { background: var(--cover); }

  .brand {
    display: flex; align-items: center; gap: 14px;
    font-weight: 600; letter-spacing: 0.08em; text-transform: uppercase;
  }
  .brand-mark { background: var(--gold); flex: none; }

  .letterhead .brand {
    position: absolute; top: 70px; left: 0; right: 0;
    justify-content: center;
    color: var(--ink); font-size: 22px;
  }
  .letterhead .brand-mark { width: 34px; height: 34px; }

  .cover .brand {
    position: absolute; top: 50%; left: 0; right: 0;
    transform: translateY(-50%);
    justify-content: center;
    color: #ffffff; font-size: 40px;
  }
  .cover .brand-mark { width: 60px; height: 60px; }

  .contacts {
    position: absolute; left: 36px; right: 30px; bottom: 42px;
    display: flex; justify-content: space-between; align-items: center;
    list-style: none;
    font-size: 9.5px; color: var(--muted); font-weight: 500;
  }
  .contacts li { display: flex; align-items: center; gap: 7px; line-height: 1.35; }
  .contacts svg { width: 14px; height: 14px; flex: none; }

  .base-band {
    position: absolute; left: 0; right: 0; bottom: 0; height: 14px;
  }
  .base-band svg { display: block; width: 100%; height: 100%; }
</style>
</head>
<body>
  <main class="folder">
    <section class="letterhead">
      <div class="brand"><span class="brand-mark"></span>Vallora Imóveis</div>

      <ul class="contacts">
        <li>
          <svg viewBox="0 0 14 14"><circle cx="7" cy="7" r="7" fill="#f4b22c"/><path d="M4.6 3.8l1.3 1.3-.7.9c.5 1 1.3 1.8 2.3 2.3l.9-.7 1.3 1.3-.8 1.2C6.7 10 4 7.3 3.7 4.6z" fill="#fff"/></svg>
          (00) 0000-0000
        </li>
        <li>
          <svg viewBox="0 0 14 14"><circle cx="7" cy="7" r="7" fill="#f4b22c"/><rect x="3.6" y="4.6" width="6.8" height="4.8" fill="none" stroke="#fff" stroke-width="0.9"/><path d="M3.6 4.8L7 7.3l3.4-2.5" fill="none" stroke="#fff" stroke-width="0.9"/></svg>
          valloraimoveis@email.com
        </li>
        <li>
          <svg viewBox="0 0 14 14"><circle cx="7" cy="7" r="7" fill="#f4b22c"/><rect x="4" y="4" width="6" height="6" fill="none" stroke="#fff" stroke-width="0.9"/></svg>
          @valloraimoveis
        </li>
        <li>
          <svg viewBox="0 0 14 14"><circle cx="7" cy="7" r="7" fill="#f4b22c"/><path d="M7 3.3a2.4 2.4 0 0 1 2.4 2.4C9.4 7.6 7 10.6 7 10.6S4.6 7.6 4.6 5.7A2.4 2.4 0 0 1 7 3.3z" fill="#fff"/><circle cx="7" cy="5.7" r="0.9" fill="#f4b22c"/></svg>
          <span>Endereço aqui, nº 00<br>Cidade - UF</span>
        </li>
      </ul>
    </section>

    <section class="cover">
      <div class="brand"><span class="brand-mark"></span>Vallora Imóveis</div>
    </section>

    <div class="base-band">
      <svg viewBox="0 0 1100 14" preserveAspectRatio="none">
        <path d="M0 11 H520 Q540 11 550 4 H1100 V14 H0 Z" fill="#f4b22c"/>
      </svg>
    </div>
  </main>
</body>
</html>
```